Home inspection business! professional look attracting customers just by looks. Read must haves

its a new business I started on my own for home inspections I would like something very professional to give to real estate agents and clients, its going to have my license number on it my business phone number my name my website as well etc on the back side it will be servicing areas and also what kind of services I offer I also have a business card from someone else the way I would like mine to be. I will attach my logo

Home Inspection

listed in nice to haves

• phone number - 555 293 8471
• website- hollowpinecheck.com
• license number #2938475610
• my name Gavin keropulis
• picture of my logo and me on the front
• on the back of the card. stating I am servicing All of New York and Long Island
• also services I will offer will be home inspection -mold inspection -lead inspection -radon inspection -Termite Inspection -Infared Scan.
• and also we provide inspections for single family homes condos co-ops town-homes
• and commercial property
• same colors as the logos and also if you recommend fonts to look like the logo not sure up to you

```html
<!DOCTYPE html>
<html lang="en">
<head>
<meta charset="utf-8">
<title>Hollow Pine Home Inspectors – Business Card</title>
<link rel="stylesheet" href="https://fonts.googleapis.com/css2?family=Montserrat:wght@500;600&family=Open+Sans:wght@400;600&display=swap">
<style>
  :root {
    --canvas: #e4e5e7;
    --card: #1f2023;
    --card-edge: #2a2b2f;
    --pattern: #26272b;
    --grey: #8a8c90;
    --light: #c9cacd;
    --blue: #2ea3f2;
    --rule: #45464b;
  }
  * { box-sizing: border-box; margin: 0; padding: 0; }
  html, body { width: 1200px; height: 1108px; overflow: hidden; background: var(--canvas); }
  .canvas {
    width: 1200px; height: 1108px;
    display: flex; justify-content: center; align-items: center; gap: 80px;
  }
  .card {
    width: 440px; height: 720px;
    background: var(--card);
    border-radius: 26px;
    position: relative;
    overflow: hidden;
    box-shadow: 0 18px 40px rgba(0,0,0,.25);
    text-align: center;
  }

  /* Front */
  .brand {
    position: absolute; top: 190px; left: 0; right: 0;
    display: flex; justify-content: center; align-items: center; gap: 14px;
  }
  .brand-dot { width: 16px; height: 16px; border-radius: 50%; background: var(--blue); }
  .brand-name {
    font-family: "Montserrat", sans-serif; font-weight: 600;
    font-size: 28px; line-height: 1.2; letter-spacing: 1px;
    color: var(--grey); text-transform: uppercase; text-align: left;
  }
  .contact { position: absolute; top: 430px; left: 0; right: 0; }
  .person-name {
    font-family: "Montserrat", sans-serif; font-weight: 600;
    font-size: 27px; letter-spacing: .5px; text-transform: uppercase;
  }
  .person-name .first { color: var(--grey); }
  .person-name .last { color: var(--blue); }
  .rule { width: 120px; height: 1px; background: var(--rule); margin: 18px auto; }
  .phone, .web, .licence {
    font-family: "Open Sans", sans-serif; font-size: 19px; color: var(--grey); line-height: 1.5;
  }
  .web .domain { color: var(--blue); }
  .licence .label { color: var(--blue); }

  /* Back */
  .pattern-area {
    position: absolute; inset: 0;
    background: radial-gradient(ellipse at 60% 30%, var(--pattern), var(--card) 75%);
  }
  .back-content { position: absolute; top: 230px; left: 40px; right: 40px; }
  .back-mark {
    display: flex; justify-content: center; align-items: center; gap: 8px;
    font-family: "Open Sans", sans-serif; font-weight: 600; font-size: 16px;
    color: var(--grey); text-transform: uppercase; letter-spacing: 1px;
  }
  .back-mark .brand-dot { width: 10px; height: 10px; }
  .area {
    margin-top: 70px;
    font-family: "Open Sans", sans-serif; font-size: 18px; line-height: 1.35;
    color: var(--blue); text-transform: uppercase;
  }
  .services {
    margin-top: 14px;
    font-family: "Open Sans", sans-serif; font-size: 18px; line-height: 1.45; color: var(--light);
  }
  .services .bullet {
    display: inline-block; width: 7px; height: 7px; border-radius: 50%;
    background: var(--blue); vertical-align: middle; margin: 0 3px;
  }
  .properties {
    margin-top: 18px;
    font-family: "Open Sans", sans-serif; font-size: 18px; line-height: 1.45; color: var(--light);
  }
</style>
</head>
<body>
<main class="canvas">
  <section class="card card-front">
    <div class="brand">
      <span class="brand-dot"></span>
      <span class="brand-name">Hollow Pine<br>Home Inspectors</span>
    </div>
    <div class="contact">
      <p class="person-name"><span class="first">Gavin</span> <span class="last">Keropulis</span></p>
      <div class="rule"></div>
      <p class="phone">555 293 8471</p>
      <p class="web">www.<span class="domain">hollowpinecheck</span>.com</p>
      <div class="rule"></div>
      <p class="licence"><span class="label">LIC NO.</span> #2938475610</p>
    </div>
  </section>

  <section class="card card-back">
    <div class="pattern-area" role="img" aria-label="Faint repeating brand mark pattern"></div>
    <div class="back-content">
      <div class="back-mark"><span class="brand-dot"></span>Hollow Pine</div>
      <p class="area">I am servicing all of New York<br>and Long Island</p>
      <p class="services">
        Home inspection<br>
        Mold Inspection<span class="bullet"></span>Lead Inspection<br>
        Radon Inspection<span class="bullet"></span>Termite Inspection<br>
        Infared Scan.
      </p>
      <p class="properties">We provide inspections for single family homes condos co-ops town-homes and commercial property</p>
    </div>
  </section>
</main>
</body>
</html>
```